Web Design Project

Psychotherapist in Private Practice
Practice name "The Quiet Harbour"
The population is professional adults seeking life coaching and change consultation
I am including a photo for inspiration ONLY - It includes the theme of light and tree branches. There does not HAVE to be a photograph . An illustration , concept or theme of nature /light / generativity / growth / creativity is acceptable
Clean sharp lines Light colors, minimalist , modern.
There is a separate project for a logo design that will become part of the web design
Here are examples of two logos/websites I like
http://www.brightmeadowcentre.ca/
http://www.openridgeadvisors.ca/

Target Market(s)

Professional adults seeking life coaching

Industry/Entity Type

Life Coaching

Requirements
Should not have
• Although the business name has 'compassion' in it, designs with hearts in it would have to be pretty stylish, subtle, mature and sophisticated to be considered.

```html
<!DOCTYPE html>
<html lang="en">
<head>
<meta charset="utf-8">
<title>The Quiet Harbour</title>
<link href="https://fonts.googleapis.com/css2?family=Open+Sans:wght@400;600;700&family=Oswald:wght@500&family=Great+Vibes&family=Questrial&display=swap" rel="stylesheet">
<style>
:root{
  --green:#5a9a16;
  --green-dark:#3b6a19;
  --green-light:#eff8e2;
  --orange:#e2820e;
  --blue:#2aa2d8;
  --text:#555;
  --dark:#333;
  --line:#d7d7d7;
  --panel:#f4f4f4;
  --sky:#a9d1e0;
}
*{margin:0;padding:0;box-sizing:border-box}
html,body{width:1200px;height:2304px;overflow:hidden}
body{position:relative;background:#fff;font-family:"Open Sans",Arial,sans-serif;color:var(--text)}
.abs{position:absolute}

/* header */
.site-header{left:0;top:0;width:1200px;height:108px;background:linear-gradient(#fff,#fbf7ea)}
.brand{left:144px;top:18px;display:flex;align-items:center;gap:12px}
.brand-dot{width:60px;height:60px;border-radius:50%;background:#7fb53a}
.brand-name{font-weight:600;font-size:22px;line-height:23px;color:var(--orange);width:150px}
.search{left:476px;top:8px;width:206px;height:24px;border-bottom:1px solid #ccc;font-size:11px;color:#aaa;padding:5px 0}
.search svg{position:absolute;right:4px;top:4px}
.help-link{left:708px;top:11px;font-size:12px;font-weight:600;color:var(--blue);white-space:nowrap}
.phone{left:938px;top:5px;font-size:20px;font-weight:600;color:var(--dark);display:flex;align-items:center;gap:6px}
.main-nav{left:501px;top:60px;display:flex;gap:2px;font-size:17px;color:#444;white-space:nowrap}
.main-nav a{color:inherit;text-decoration:none;padding:5px 10px;height:34px}
.main-nav a.active{background:var(--green);color:#fff}

/* hero */
.hero{left:0;top:108px;width:1200px;height:492px;background:radial-gradient(ellipse at 55% 20%,#d6ecb0 0%,#6fa83a 35%,#2f5e1c 75%,#24481a 100%)}
.hero-title{left:215px;top:282px;font-family:"Questrial",sans-serif;font-size:44px;line-height:48px;color:#fff;font-weight:700}
.slider-tab{left:543px;top:566px;width:115px;height:34px;background:var(--green-light);border-radius:8px 8px 0 0;display:flex;gap:6px;justify-content:center;align-items:center}
.slider-tab i{width:11px;height:11px;border-radius:50%;background:#c9c9c9}
.slider-tab i.on{background:var(--green)}

/* welcome */
.welcome{left:0;top:600px;width:1200px;height:238px;background:var(--green-light);text-align:center}
.welcome-script{font-family:"Great Vibes",cursive;font-size:32px;color:#222;margin-top:14px;line-height:36px}
.welcome-title{font-weight:700;font-size:32px;color:var(--orange);letter-spacing:1px;line-height:36px}
.welcome p{width:920px;margin:14px auto 0;font-size:14.5px;line-height:23px}
.welcome p+p{margin-top:12px}

/* events */
.section-bar{background:linear-gradient(#6cb21e,#4f8d12);color:#fff;font-family:"Oswald",sans-serif;font-size:22px;padding-left:16px;line-height:38px}
.events-bar{left:140px;top:860px;width:615px;height:38px}
.event{left:140px;width:615px;height:112px}
.event-photo{position:absolute;left:0;top:0;width:148px;height:98px;border:4px solid #e6e6e6}
.event h3{position:absolute;left:167px;top:0;font-size:16px;font-weight:400;color:#222}
.event p{position:absolute;left:167px;top:34px;width:440px;font-size:11.5px;line-height:22px}
.more{color:var(--orange);font-size:10px}
.event-meta{position:absolute;left:167px;top:86px;width:448px;height:24px;border-bottom:1px dashed #ccc;font-size:11px;display:flex;justify-content:space-between}
.event-meta span{display:flex;gap:6px;align-items:flex-start}
.ico{display:inline-block;width:12px;height:11px;background:#bbb;margin-top:2px}

/* gallery */
.gallery{left:140px;top:1469px;width:615px;height:455px;background:#f2f2f2;border:1px solid #e0e0e0;border-radius:6px}
.gallery-bar{left:140px;top:1469px;width:615px;height:42px;border-radius:6px 6px 0 0;text-align:center;padding:0;line-height:42px}
.gallery-notch{left:438px;top:1510px}
.thumb{width:179px;height:111px;border:4px solid #e3e3e3}
.view-all-btn{left:407px;top:1912px;width:76px;height:31px;background:var(--orange);color:#fff;font-size:12px;font-weight:700;text-align:center;line-height:31px;border-radius:3px}

/* side panels */
.panel{left:783px;width:277px;border:1px solid #e0e0e0;background:#f5f5f5}
.panel-head{height:50px;background:linear-gradient(#fff,#ececec);font-family:"Oswald",sans-serif;font-size:22px;color:#222;padding:10px 14px;position:relative}
.tag{position:absolute;right:12px;top:16px;background:#a9d1e0;color:#fff;font-family:"Open Sans",sans-serif;font-size:9px;font-weight:700;padding:2px 8px}
.blog-item{padding:0 16px;margin-top:20px}
.blog-item h4{font-size:11.5px;color:var(--blue);font-weight:600}
.blog-item small{display:block;font-size:9px;color:#999;margin:2px 0 4px}
.blog-item p{font-size:11.5px;line-height:17px}
.cal{margin:14px 0 0 27px;width:222px}
.cal-head{background:#666;color:#fff;font-size:12px;text-align:center;height:32px;line-height:32px;letter-spacing:1px;display:flex;justify-content:space-between;padding:0 10px}
.cal table{width:222px;border-collapse:collapse;background:#fff;font-size:14px;color:#222}
.cal th{font-size:9px;color:#999;font-weight:400;height:22px;border:1px solid #eee}
.cal td{height:32px;text-align:center;border:1px solid #ddd}
.cal td.today{background:var(--orange);color:#fff;font-weight:700}
.newsletter{left:783px;top:1607px;width:277px;height:154px;background:var(--sky);padding:14px 18px}
.newsletter h3{font-family:"Oswald",sans-serif;font-size:22px;color:#fff;font-weight:500;display:flex;gap:10px;align-items:center}
.email-field{margin-top:14px;height:34px;background:#fff;font-size:11px;color:#999;padding:9px 12px}
.subscribe{margin-top:10px;height:34px;background:linear-gradient(#16607a,#0c4357);color:#fff;font-family:"Oswald",sans-serif;font-size:18px;text-align:center;line-height:34px}
.social-box{left:783px;top:1776px;width:277px;height:250px;background:#fff;border:1px solid #bbb;font-size:11px;color:#333;z-index:2}
.social-box .title{font-weight:700;background:#eee;padding:3px 6px;border-bottom:1px solid #ccc}
.page-card{display:flex;gap:10px;padding:8px 10px}
.page-dot{width:50px;height:50px;border-radius:50%;background:#7fb53a}
.page-card b{color:#2a5aa0;font-weight:600}
.like{display:inline-block;margin-top:6px;border:1px solid #aaa;background:#f1f1f1;padding:0 6px;font-size:10px}
.fans{display:grid;grid-template-columns:repeat(5,48px);gap:4px;padding:4px 10px}
.fans span{height:48px;background:linear-gradient(#b58a6e,#6b5446)}
.plugin-note{position:absolute;bottom:0;left:0;right:0;border-top:1px solid #ddd;font-size:9px;color:#777;padding:3px 8px}

/* social band */
.tweet-band{left:0;top:1997px;width:1200px;height:169px;background:linear-gradient(#fafafa,#eaeaea);text-align:center}
.tweet-dot{width:28px;height:28px;border-radius:50%;background:var(--blue);margin:24px auto 14px}
.tweet-band p{font-size:16px;line-height:29px;color:#777}
.tweet-band a{color:var(--blue);text-decoration:underline}

/* footer */
.site-footer{left:0;top:2166px;width:1200px;height:138px;background:var(--green-dark);color:#fff}
.foot-links{left:140px;top:32px;font-size:12px;line-height:20px}
.foot-contact{top:30px;font-size:12px;line-height:20px}
.foot-contact b{font-weight:400;font-size:16px;line-height:24px}
.foot-social{left:940px;top:44px;display:flex;gap:8px}
.foot-social span{width:26px;height:26px;background:#557d2b}
.copyright{left:0;top:112px;width:1200px;text-align:center;font-size:11px;color:#6f944a}
</style>
</head>
<body>

<header class="abs site-header">
  <div class="abs brand"><span class="brand-dot"></span><span class="brand-name">The Quiet Harbour</span></div>
  <div class="abs search">Search
    <svg width="16" height="16" viewBox="0 0 16 16"><circle cx="6" cy="6" r="4.5" fill="none" stroke="#555" stroke-width="2"/><path d="M9.5 9.5 14 14" stroke="#555" stroke-width="2.5"/></svg>
  </div>
  <div class="abs help-link">FIND OUT HOW WE CAN HELP YOU</div>
  <div class="abs phone">
    <svg width="12" height="20" viewBox="0 0 12 20"><path d="M9 1H4C2 1 1 3 1 10s1 9 3 9h5v-5H6c-.6-1-.6-7 0-8h3z" fill="var(--orange)"/></svg>
    416-555-0192
  </div>
  <nav class="abs main-nav">
    <a class="active" href="#">HOME</a><a href="#">MEET OUR TEAM</a><a href="#">BLOG</a><a href="#">SCHEDULE &amp; FEES</a><a href="#">CONTACT</a>
  </nav>
</header>

<section class="abs hero" role="img" aria-label="Photograph of a woman relaxing on the grass in a sunlit green park with trees"></section>
<h1 class="abs hero-title">Lorem ipsum dolor<br>sit amet,</h1>
<div class="abs slider-tab"><i class="on"></i><i></i><i></i><i></i><i></i></div>

<section class="abs welcome">
  <div class="welcome-script">Welcome to</div>
  <h2 class="welcome-title">THE QUIET HARBOUR</h2>
  <p>We combine psychotherapy with Mindfulness to help you feel better and reach your goals. You can choose from individual counselling, several types of . We combine traditional psychotherapy with mindfulness to help you. Patient ratings confirm we are effective.</p>
  <p>Contact us if you need a therapist or group to help you with depression, anxiety, stress, borderline personality disorder or other problems. Our services are available in downtown Toronto, Queen West, North York, The Annex, St. Lawrence Market, South Rosedale and online. We offer therapy services in English, German, Serbian, Croatian, Urdu, Hindi, Punjabi and Farsi.</p>
</section>

<div class="abs section-bar events-bar">Upcoming Events</div>

<article class="abs event" style="top:929px">
  <div class="event-photo" role="img" aria-label="Photo of a counselling session with clipboard" style="background:linear-gradient(135deg,#e7e2da,#a9b6c2)"></div>
  <h3>Lorem Ipsum is of the printing</h3>
  <p>Lorem Ipsum passages, and an recently with desktop publishing wathe Verdel Makerprinting and typesetting when to setting anspecimen book. <span class="more">READ MORE...</span></p>
  <div class="event-meta"><span><i class="ico"></i>Date: 26 July 2013</span><span><i class="ico"></i>Comments: 125</span></div>
</article>
<article class="abs event" style="top:1058px">
  <div class="event-photo" role="img" aria-label="Photo of a support group seated in a circle" style="background:linear-gradient(135deg,#8a7b6c,#3f3a36)"></div>
  <h3>Lorem Ipsum is of the printing</h3>
  <p>Lorem Ipsum passages, and an recently with desktop publishing wathe Verdel Makerprinting and typesetting when to setting anspecimen book. <span class="more">READ MORE...</span></p>
  <div class="event-meta"><span><i class="ico"></i>Date: 26 July 2013</span><span><i class="ico"></i>Comments: 125</span></div>
</article>
<article class="abs event" style="top:1187px">
  <div class="event-photo" role="img" aria-label="Photo of two women talking" style="background:linear-gradient(135deg,#d9b79a,#9c6a4e)"></div>
  <h3>Lorem Ipsum is of the printing</h3>
  <p>Lorem Ipsum passages, and an recently with desktop publishing wathe Verdel Makerprinting and typesetting when to setting anspecimen book. <span class="more">READ MORE...</span></p>
  <div class="event-meta"><span><i class="ico"></i>Date: 26 July 2013</span><span><i class="ico"></i>Comments: 125</span></div>
</article>
<article class="abs event" style="top:1313px">
  <div class="event-photo" role="img" aria-label="Photo of a therapist with a client on a sofa" style="background:linear-gradient(135deg,#f2f2f2,#9a9a9a)"></div>
  <h3>Lorem Ipsum is of the printing</h3>
  <p>Lorem Ipsum passages, and an recently with desktop publishing wathe Verdel Makerprinting and typesetting when to setting anspecimen book. <span class="more">READ MORE...</span></p>
  <div class="event-meta"><span><i class="ico"></i>Date: 26 July 2013</span><span><i class="ico"></i>Comments: 125</span></div>
</article>

<section class="abs gallery"></section>
<div class="abs section-bar gallery-bar">PHOTOGALLERY</div>
<svg class="abs gallery-notch" width="20" height="10" viewBox="0 0 20 10"><path d="M0 0h20L10 10z" fill="#4f8d12"/></svg>
<div class="abs thumb" style="left:163px;top:1536px;background:linear-gradient(135deg,#eee,#8d8d8d)" role="img" aria-label="Photo of a consultation in an office"></div>
<div class="abs thumb" style="left:359px;top:1536px;background:linear-gradient(135deg,#e9ddd0,#b5513a)" role="img" aria-label="Photo of a therapy conversation"></div>
<div class="abs thumb" style="left:553px;top:1536px;background:linear-gradient(135deg,#e6d8cc,#7d8a8f)" role="img" aria-label="Photo of comforting hands"></div>
<div class="abs thumb" style="left:163px;top:1663px;background:linear-gradient(#9c9f7a,#4e6a2a)" role="img" aria-label="Photo of a woman meditating outdoors"></div>
<div class="abs thumb" style="left:359px;top:1663px;background:linear-gradient(#c4d9a5,#4f7b2c)" role="img" aria-label="Photo of a person stretching in a park"></div>
<div class="abs thumb" style="left:553px;top:1663px;background:linear-gradient(#a8c483,#3a6d2b)" role="img" aria-label="Photo of yoga on a mat in the grass"></div>
<div class="abs thumb" style="left:163px;top:1789px;background:linear-gradient(135deg,#d6a88a,#3a9b9a)" role="img" aria-label="Photo of a family embracing"></div>
<div class="abs thumb" style="left:359px;top:1789px;background:linear-gradient(135deg,#efe5dc,#a88c72)" role="img" aria-label="Photo of a counsellor with a client"></div>
<div class="abs thumb" style="left:553px;top:1789px;background:linear-gradient(135deg,#f0ebe6,#6b5a4f)" role="img" aria-label="Photo of two women in a session"></div>
<div class="abs view-all-btn">VIEW ALL</div>

<aside class="abs panel" style="top:858px;height:403px">
  <div class="panel-head">Our Blogs<span class="tag">VIEW ALL</span></div>
  <div class="blog-item"><h4>Lorem Ipsum is of the printing</h4><small>26 july 2013</small><p>Lorem Ipsum is simply dummy text printing when anspecimen book.content here', making it readable English.</p></div>
  <div class="blog-item" style="margin-top:26px"><h4>Lorem Ipsum is of the printing</h4><small>26 july 2013</small><p>Lorem Ipsum is simply dummy text printing when anspecimen book.content here', making it readable English.</p></div>
  <div class="blog-item" style="margin-top:26px"><h4>Lorem Ipsum is of the printing</h4><small>26 july 2013</small><p>Lorem Ipsum is simply dummy text printing when anspecimen book.content here', making it readable English.</p></div>
</aside>

<aside class="abs panel" style="top:1279px;height:311px">
  <div class="panel-head">Calendar</div>
  <div class="cal">
    <div class="cal-head"><span>&#8249;</span><span>AUGUST 2012</span><span>&#8250;</span></div>
    <table>
      <tr><th>SUN</th><th>MON</th><th>TUE</th><th>WED</th><th>THU</th><th>FRI</th><th>SAT</th></tr>
      <tr><td></td><td></td><td></td><td>1</td><td>2</td><td class="today">3</td><td>4</td></tr>
      <tr><td>5</td><td>6</td><td>7</td><td>8</td><td>9</td><td>10</td><td>11</td></tr>
      <tr><td>12</td><td>13</td><td>14</td><td>15</td><td>16</td><td>17</td><td>18</td></tr>
      <tr><td>19</td><td>20</td><td>21</td><td>22</td><td>23</td><td>24</td><td>25</td></tr>
      <tr><td>26</td><td>27</td><td>28</td><td>29</td><td>30</td><td>31</td><td></td></tr>
    </table>
  </div>
</aside>

<aside class="abs newsletter">
  <h3><svg width="28" height="22" viewBox="0 0 28 22"><rect x="1" y="5" width="26" height="16" fill="#fff"/><path d="M1 5l13 9 13-9" fill="none" stroke="var(--sky)" stroke-width="2"/></svg>STAY IN TOUCH</h3>
  <div class="email-field">Enter your email address</div>
  <div class="subscribe">SUBSCRIBE</div>
</aside>

<aside class="abs social-box">
  <div class="title">Find us on Friendsbook</div>
  <div class="page-card"><span class="page-dot"></span><div><b>The Quiet Harbour</b><br><span class="like">Like</span></div></div>
  <div style="padding:0 10px">2,994 people like The Quiet Harbour</div>
  <div class="fans"><span></span><span></span><span></span><span></span><span></span><span></span><span></span><span></span><span></span><span></span></div>
  <div class="plugin-note">Friendsbook social plugin</div>
</aside>

<section class="abs tweet-band">
  <div class="tweet-dot"></div>
  <p>Mindfulness Reduces Anxiety and Stress in Bipolar Disorder Follow us at <a href="#">Chirper.com/quietmindful</a> for quotes and<br>sayings about Mindfulness or at <a href="#">Chirper.com/StillPoint</a> Reminder for daily reminders to be Mindful.</p>
</section>

<footer class="abs site-footer">
  <div class="abs foot-links">Home &nbsp;|&nbsp; Meet our Team &nbsp;|&nbsp; Blog<br>Schedule &amp; Fees</div>
  <div class="abs foot-contact" style="left:422px;display:flex;gap:8px">
    <svg width="14" height="34" viewBox="0 0 12 20"><path d="M9 1H4C2 1 1 3 1 10s1 9 3 9h5v-5H6c-.6-1-.6-7 0-8h3z" fill="#fff"/></svg>
    <div>Phone :<br><b>0198 765 432</b></div>
  </div>
  <div class="abs foot-contact" style="left:658px">Email:<br><b style="font-size:13px">info@quietharbour.ca</b></div>
  <div class="abs foot-social"><span></span><span></span><span></span></div>
  <div class="abs copyright">Copyright © 2013 The Quiet Harbour all right reserved.</div>
</footer>

</body>
</html>
```